Red Lantern Take Away, take away menu

We want to use the double sided flyer design to produce a bulk amount of take away menus, which incorporate full contact details for our two shopfronts. We are a Take Away business in Wagga Wagga NSW, with two store, one which opened last year. We may also look to use these flyers for a letter box drop into the future. Our detailed menu can be found at redlanterntakeaway.com.au and contact details for both shops can be found on our facebook page Red Lantern Take Away.
Updates

Hi all, Please note that the menu prices on our website are not the current prices. Please contact me with an email so I can send through a correct copy. I will be extending the due date to compensate for this oversight. Thanks.

Reason: Deadline is being extended as the old prices are still advertised on our menu (@redlanterntakeaway.com) . Please contact me via email for a copy of the up to date pricing.

Hi all, Please note that a file has been updated to the brief with current pricing. Please use this pricing in any proposals. Please don't use any of the combo deals in your proposals as they may be subject to change. Please also have a disclaimer at the bottom of your flyer that states "Please note: Prices may be subject to change". Sorry about the dripping of information as this is our first time using sketch forge. Thanks.

Industry/Entity Type

Business

```html
<!DOCTYPE html>
<html lang="en">
<head>
<meta charset="utf-8">
<title>Red Lantern Take Away – Menu</title>
<link rel="stylesheet" href="https://fonts.googleapis.com/css2?family=Bungee+Shade&family=Didact+Gothic&display=swap">
<style>
:root{
  --page-bg:#ffffff;
  --canvas-bg:#ffffff;
  --brand-blue:#1f43a0;
  --ink-blue:#2a45b0;
  --pale-blue:#c7cfea;
  --mid-blue:#8d9bd6;
  --white:#ffffff;
  --shadow:rgba(0,0,0,.28);
}
*{box-sizing:border-box;margin:0;padding:0}
html,body{width:1200px;height:848px;overflow:hidden;background:var(--canvas-bg)}
body{position:relative;font-family:"Didact Gothic",sans-serif}
.page{position:absolute;top:45px;width:525px;height:742px;overflow:hidden;box-shadow:4px 4px 8px var(--shadow)}
.page--cover{left:47px;background:var(--brand-blue);color:var(--white)}
.page--menu{left:628px;background:var(--page-bg);color:var(--ink-blue)}

/* cover */
.cover-emblem{position:absolute;left:50px;top:40px;width:425px;height:125px;border-radius:60px;
  background:linear-gradient(90deg,rgba(141,155,214,.55),rgba(141,155,214,.8))}
.cover-title{position:absolute;left:0;top:0;width:525px;height:742px}
.cover-title text{font-family:"Didact Gothic",sans-serif;font-size:31px;fill:var(--white);letter-spacing:1px}
.cover-heading{position:absolute;left:0;width:100%;top:262px;text-align:center;font-family:"Bungee Shade",sans-serif;font-size:60px;line-height:70px;color:var(--white)}
.store{position:absolute;left:0;width:100%;text-align:center}
.store__address{font-size:16px;line-height:20px}
.store__phone{font-size:20px;line-height:26px;display:flex;justify-content:center;align-items:center;gap:6px;margin-top:4px}
.store__phone svg{width:20px;height:20px}
.hours{margin:6px auto 0;display:grid;grid-template-columns:auto auto;column-gap:26px;justify-content:center;font-size:12px;line-height:14.8px;text-align:left}
.store--one{top:367px}
.store--two{top:470px}
.online{position:absolute;left:0;width:100%;top:617px;text-align:center;font-size:14px;line-height:20px}
.online__social{display:flex;justify-content:center;align-items:center;gap:5px}
.online__dot{width:15px;height:15px;border-radius:50%;background:var(--white)}
.waves{position:absolute;left:0;bottom:0;width:525px;height:70px;
  background:linear-gradient(180deg,rgba(141,155,214,.3),rgba(199,207,234,.85))}

/* menu page */
.menu-decor{position:absolute;left:0;top:580px;width:525px;height:162px;border-radius:80px 0 0 0;
  background:linear-gradient(90deg,rgba(199,207,234,.85),rgba(199,207,234,.6))}
.menu-section{position:absolute;width:207px;font-size:12px;line-height:14.8px}
.menu-section__title{font-family:"Bungee Shade",sans-serif;font-size:19px;line-height:22px;color:var(--ink-blue);margin-bottom:0}
.menu-row{display:flex;justify-content:space-between;white-space:nowrap}
.menu-row small{font-size:9px}
.menu-row--wrap{white-space:normal;line-height:11px;margin-bottom:3px}
.menu-sub{font-weight:bold;margin-top:6px}
.gap{height:8px}
.hot{left:40px;top:42px}
.seafood{left:282px;top:42px}
.burgers{left:40px;top:382px}
.sandwiches{left:282px;top:382px}
</style>
</head>
<body>

<section class="page page--cover">
  <div class="cover-emblem" role="img" aria-label="Stylised fish with fork and spoon emblem"></div>
  <svg class="cover-title" viewBox="0 0 525 742" aria-label="Red Lantern Take Away">
    <defs><path id="title-arc" d="M 68 240 Q 250 178 472 188"/></defs>
    <text><textPath href="#title-arc" startOffset="50%" text-anchor="middle">Red Lantern Take Away</textPath></text>
  </svg>
  <h1 class="cover-heading">MENU</h1>

  <div class="store store--one">
    <p class="store__address">42 Harbour St</p>
    <p class="store__phone"><svg viewBox="0 0 24 24" fill="#fff"><path d="M6.6 10.8a15 15 0 0 0 6.6 6.6l2.2-2.2c.3-.3.7-.4 1-.2 1.1.4 2.3.6 3.6.6.6 0 1 .4 1 1V20c0 .6-.4 1-1 1A17 17 0 0 1 3 4c0-.6.4-1 1-1h3.5c.6 0 1 .4 1 1 0 1.3.2 2.5.6 3.6.1.3 0 .7-.2 1z"/></svg>69 555 104</p>
    <div class="hours"><span>Sat - Wed</span><span>8 AM - 8 PM</span><span>Thurs - Fri</span><span>8 AM - 9 PM</span></div>
  </div>

  <div class="store store--two">
    <p class="store__address">Shop 12 Riverside Plaza</p>
    <p class="store__phone"><svg viewBox="0 0 24 24" fill="#fff"><path d="M6.6 10.8a15 15 0 0 0 6.6 6.6l2.2-2.2c.3-.3.7-.4 1-.2 1.1.4 2.3.6 3.6.6.6 0 1 .4 1 1V20c0 .6-.4 1-1 1A17 17 0 0 1 3 4c0-.6.4-1 1-1h3.5c.6 0 1 .4 1 1 0 1.3.2 2.5.6 3.6.1.3 0 .7-.2 1z"/></svg>69 555 217</p>
    <div class="hours"><span>Mon</span><span>8 AM - 5 PM</span><span>Tues - Thurs</span><span>8 AM - 7:30 PM</span><span>Fri - Sun</span><span>8 AM - 8 PM</span></div>
  </div>

  <div class="online">
    <p class="online__social"><span class="online__dot"></span>/redlanterntakeaway</p>
    <p>redlanterntakeaway.com</p>
  </div>
  <div class="waves" role="img" aria-label="Layered ocean waves"></div>
</section>

<section class="page page--menu">
  <div class="menu-decor" role="img" aria-label="Faint fish with fork and spoon emblem"></div>

  <div class="menu-section hot">
    <h2 class="menu-section__title">Hot Food</h2>
    <p class="menu-row"><span>Minimum Chips</span><span>$3.00</span></p>
    <p class="menu-row"><span>Dim Sim - Meat</span><span>$1.20</span></p>
    <p class="menu-row"><span>Dim Sim - Veggie</span><span>$1.30</span></p>
    <p class="menu-row"><span>Cabbage Roll</span><span>$2.60</span></p>
    <p class="menu-row"><span>Spring Roll</span><span>$2.60</span></p>
    <p class="menu-row"><span>Mini Spring Roll</span><span>$1.20</span></p>
    <p class="menu-row"><span>Chicken D/Stick</span><span>$3.00</span></p>
    <p class="menu-row"><span>Chicken Wing Ding</span><span>$1.40</span></p>
    <p class="menu-row"><span>Chicken Chippies (10 )</span><span>$2.00</span></p>
    <p class="menu-row"><span>Pineapple Fritter</span><span>$1.80</span></p>
    <p class="menu-row"><span>Chicken Nuggets</span><span>$0.80</span></p>
    <p class="menu-row"><span>Corn Jacks</span><span>$2.30</span></p>
    <p class="menu-row"><span>Corn Fritter</span><span>$0.80</span></p>
    <p class="menu-row"><span>Chicken Corn Roll</span><span>$2.50</span></p>
    <p class="menu-row"><span>Beef Croquets</span><span>$1.20</span></p>
    <p class="menu-row"><span>Chicken Garlic Balls</span><span>$1.30</span></p>
    <p class="menu-row"><span>Potato Scallops</span><span>$0.90</span></p>
    <p class="menu-row"><span>Potato Gems (12)</span><span>$1.80</span></p>
    <p class="menu-row"><span>Battered Sav</span><span>$2.40</span></p>
  </div>

  <div class="menu-section seafood">
    <h2 class="menu-section__title">Seafood</h2>
    <p class="menu-row"><span>Fish - Battered</span><span>$6.50</span></p>
    <p class="menu-row"><span>Fish - Grilled</span><span>$7.00</span></p>
    <p class="menu-row"><span>Fish - Crumbed</span><span>$7.50</span></p>
    <p class="menu-row"><span>Fish - Cocktail</span><span>$1.30</span></p>
    <p class="menu-row"><span>Barramundi</span><span>$7.50</span></p>
    <div class="gap"></div>
    <p class="menu-row"><span>Grilled Fish &amp; Chips</span><span>$8.50</span></p>
    <p class="menu-row"><span>Grilled Fish &amp; Salad</span><span>$9.50</span></p>
    <p class="menu-row"><span>Grilled Fish, Salad &amp; Chips</span><span>$11.00</span></p>
    <p class="menu-row"><span>Barramundi &amp; Chips</span><span>$9.00</span></p>
    <p class="menu-row"><span>Barramundi &amp; Salad</span><span>$10.00</span></p>
    <p class="menu-row"><span>Barramundi, Salad &amp; Chips</span><span>$11.50</span></p>
    <p class="menu-sub">Seafood Basket</p>
    <p class="menu-row"><span>Fish Cake</span><span>$2.80</span></p>
    <p class="menu-row"><span>Prawn Cutlet</span><span>$2.20</span></p>
    <p class="menu-row"><span>Tassie Scallop</span><span>$1.50</span></p>
    <p class="menu-row"><span>Calamari Rings</span><span>$0.80</span></p>
    <p class="menu-row"><span>Sea Shanties</span><span>$1.20</span></p>
    <p class="menu-row"><span>Prawn Bar</span><span>$2.50</span></p>
    <p class="menu-row"><span>Seafood Stick</span><span>$2.30</span></p>
  </div>

  <div class="menu-section burgers">
    <h2 class="menu-section__title">Burgers</h2>
    <p class="menu-row"><span>Hamburger - Plain</span><span>$6.00</span></p>
    <p class="menu-row"><span>Hamburger - Egg</span><span>$6.50</span></p>
    <p class="menu-row"><span>Hamburger - Lot</span><span>$8.00</span></p>
    <p class="menu-row"><span>Cheese Burger</span><span>$5.50</span></p>
    <p class="menu-row"><span>Chicken Schnitzel - Plain</span><span>$7.00</span></p>
    <p class="menu-row"><span>Chicken Schnitzel - Lot</span><span>$9.00</span></p>
    <p class="menu-row"><span>Grilled Fish Burger</span><span>$8.50</span></p>
    <p class="menu-row"><span>Battered Fish Burger</span><span>$7.50</span></p>
    <p class="menu-row"><span>Prawn Burger</span><span>$6.00</span></p>
    <p class="menu-row"><span>Scallop Burger - Plain</span><span>$4.50</span></p>
    <p class="menu-row"><span>Scallop Burger - Lot</span><span>$6.50</span></p>
    <p class="menu-row"><span>Steak Sandwich - Plain</span><span>$7.00</span></p>
    <p class="menu-row"><span>Steak Sandwich - Lot</span><span>$9.00</span></p>
    <p class="menu-row"><span>Bacon &amp; Egg Roll</span><span>$6.00</span></p>
    <div class="gap"></div>
    <p class="menu-row"><span>Extras</span><span>$0.50</span></p>
    <p class="menu-row"><span>Pineapple</span><span>$0.50</span></p>
    <p class="menu-row"><span>Cheese</span><span>$0.50</span></p>
    <p class="menu-row"><span>Egg</span><span>$0.50</span></p>
    <p class="menu-row"><span>Bacon</span><span>$1.00</span></p>
    <p class="menu-row"><span>Salad <small>(Lettuce, Tomato, ??? - Each)</small></span><span>$0.30</span></p>
  </div>

  <div class="menu-section sandwiches">
    <h2 class="menu-section__title">Sandwiches</h2>
    <p class="menu-sub" style="margin-top:0">Toasted</p>
    <p class="menu-row"><span>Cheese</span><span>$3.00</span></p>
    <p class="menu-row"><span>Cheese &amp; Tomato</span><span>$3.50</span></p>
    <p class="menu-row"><span>Ham &amp; Cheese</span><span>$4.50</span></p>
    <p class="menu-row"><span>Ham, Cheese &amp; Tomato</span><span>$5.00</span></p>
    <p class="menu-sub">Fresh</p>
    <p class="menu-row"><span>Cheese</span><span>$2.50</span></p>
    <p class="menu-row"><span>Cheese &amp; Tomato</span><span>$3.00</span></p>
    <p class="menu-row"><span>Ham &amp; Cheese</span><span>$4.00</span></p>
    <p class="menu-row"><span>Salad <small>(inc. Cheese &amp; Mayo)</small></span><span>$4.50</span></p>
    <p class="menu-row menu-row--wrap"><span>Ham, Cheese &amp; Salad<br><small>(inc. Mayo)</small></span><span>$5.50</span></p>
    <p class="menu-sub">Rolls</p>
    <p class="menu-row"><span>Salad <small>(inc. Cheese &amp; Mayo)</small></span><span>$5.00</span></p>
    <p class="menu-row menu-row--wrap"><span>Ham, Cheese &amp; Salad<br><small>(inc. Mayo)</small></span><span>$6.00</span></p>
  </div>
</section>

</body>
</html>
```